Business Card Design Project

Card must be printed on two sides
Preference for horizontal layout
Clean images-easy to understand the offer

Loyalty Card

Buy any Juice/Smoothie/Falafel Pocket - 7th one is free

Emphasis on the 7 and FREE
Updates

Please note: We have added some more information and tried to clarify the offer.
All submissions welcome
We will have further design work to follow up this promotion.

Thank you.

Regards
Dennis

Target Market(s)

Local residents
Many singles
Age: 20-45
Male & Female
Healthy & tasty fresh food and juice - most purchases under $15
We are located close to the seaside in St Kilda Melbourne Victoria

Industry/Entity Type

Business

Requirements
Must have
• QB Logo
Address: 52 Morrow Lane St Kilda Vic 3182

6 Squares/Circles/empty logos to stamp purchases

Limit one use per customer per visit (small text)
Buy any juice/smoothie or whole falafel pocket and you will receive one item of your choice free on your 7th visit.
Offer Valid till: (blank)

Two sided: Logo (optional: Brief about the business) on front and detail on the back
Nice to have
• Design and offer that you will keep not throw away

Images need to be sharp and easy to understand the offer

Not transferable - one per customer

```html
<!DOCTYPE html>
<html lang="en">
<head>
<meta charset="utf-8">
<title>QuayBite Loyalty Card</title>
<link rel="stylesheet" href="https://fonts.googleapis.com/css2?family=Archivo+Black&family=Bangers&family=Chewy&family=Ubuntu+Condensed&family=Alfa+Slab+One&display=swap">
<style>
  :root {
    --page: #ffffff;
    --shadow: #a9a9a9;
    --front-orange: #e2791a;
    --front-red: #922a22;
    --front-rust: #b24a22;
    --brand-green: #5cc22a;
    --heading-white: #ffffff;
    --heading-pink: #f2c3bf;
    --heading-shade: #3a1a14;
    --address-ink: #3d4b7c;
    --pin-blue: #1f6fd0;
    --back-blue: #a2d2dc;
    --back-lilac: #b8b1d9;
    --offer-ink: #8c1f2f;
    --stamp-fill: #dfe892;
    --stamp-edge: #ffffff;
    --free-ink: #8a2a8c;
    --footer-ink: #1a1a1a;
  }
  * { margin: 0; padding: 0; box-sizing: border-box; }
  html, body {
    width: 1151px; height: 1200px; overflow: hidden;
    background: var(--page);
  }
  .canvas { position: relative; width: 1151px; height: 1200px; }

  .card-shadow { position: absolute; background: var(--shadow); }
  .card { position: absolute; overflow: hidden; }

  /* Front */
  .front-shadow { left: 150px; top: 101px; width: 895px; height: 504px; }
  .card-front {
    left: 122px; top: 75px; width: 896px; height: 503px;
    background: linear-gradient(100deg, var(--front-orange) 0%, #c8561e 35%, var(--front-red) 68%, var(--front-rust) 100%);
  }
  .decor-circle {
    position: absolute; left: 13px; top: 8px; width: 362px; height: 362px;
    border-radius: 50%;
    background: linear-gradient(135deg, rgba(255,255,255,0.9) 0%, rgba(255,255,255,0.35) 45%, rgba(255,255,255,0.55) 100%);
    opacity: 0.7;
  }
  .brand-name {
    position: absolute; font-family: "Archivo Black", sans-serif;
    color: var(--brand-green); white-space: nowrap;
  }
  .front-brand { left: 602px; top: 200px; font-size: 46px; letter-spacing: -1px; }
  .card-title {
    position: absolute; left: 440px; top: 280px;
    font-family: "Bangers", sans-serif; font-size: 72px; letter-spacing: 2px;
    color: var(--heading-white);
    text-shadow: 4px 4px 0 var(--heading-shade);
    white-space: nowrap;
  }
  .card-title .accent { color: var(--heading-pink); }
  .address {
    position: absolute; left: 78px; top: 432px; display: flex; align-items: center; gap: 12px;
    font-family: "Archivo Black", sans-serif; font-size: 35px; color: var(--address-ink);
    text-shadow: -1px -1px 0 #fff, 1px -1px 0 #fff, -1px 1px 0 #fff, 1px 1px 0 #fff;
    white-space: nowrap;
  }
  .pin-icon { width: 26px; height: 42px; }

  /* Back */
  .back-shadow { left: 148px; top: 657px; width: 894px; height: 503px; }
  .card-back {
    left: 122px; top: 632px; width: 895px; height: 503px;
    background: radial-gradient(ellipse at 50% 50%, var(--back-lilac) 0%, var(--back-blue) 75%);
  }
  .offer {
    position: absolute; left: 54px; top: 40px; width: 800px;
    font-family: "Chewy", sans-serif; font-size: 30px; line-height: 44px;
    color: var(--offer-ink);
  }
  .stamp {
    position: absolute; width: 112px; height: 112px;
    background: var(--stamp-fill); border: 3px solid var(--stamp-edge);
    border-radius: 0 50% 50% 50%;
  }
  .stamp-free {
    border-radius: 50%; display: flex; align-items: center; justify-content: center;
    font-family: "Alfa Slab One", serif; font-size: 26px; color: var(--free-ink); letter-spacing: 1px;
  }
  .back-brand { left: 666px; top: 262px; font-size: 31px; letter-spacing: -0.5px; }
  .footer-note {
    position: absolute; top: 446px;
    font-family: "Ubuntu Condensed", sans-serif; font-size: 32px; color: var(--footer-ink);
    white-space: nowrap;
  }
  .not-transferable { left: 31px; }
  .valid-till { left: 495px; }
  .valid-field {
    position: absolute; left: 688px; top: 448px; width: 188px; height: 32px;
    background: #fff; border-radius: 16px;
  }
</style>
</head>
<body>
<div class="canvas">
  <div class="card-shadow front-shadow"></div>
  <section class="card card-front">
    <div class="decor-circle"></div>
    <div class="brand-name front-brand">QuayBite</div>
    <h1 class="card-title">LOYALTY <span class="accent">CARD</span></h1>
    <p class="address">
      <svg class="pin-icon" viewBox="0 0 26 42" aria-hidden="true">
        <path d="M13 0C5.8 0 0 5.8 0 13c0 9 13 29 13 29s13-20 13-29C26 5.8 20.2 0 13 0z" fill="var(--pin-blue)"/>
        <circle cx="13" cy="13" r="5" fill="#fff"/>
      </svg>
      52 Morrow Lane St Kilda Vic 3182
    </p>
  </section>

  <div class="card-shadow back-shadow"></div>
  <section class="card card-back">
    <p class="offer">Buy any Juice, Smoothie or Whole Falafel pocket and you will receive any one Free after your 6th purchase.</p>
    <div class="stamp" style="left:78px;top:153px"></div>
    <div class="stamp" style="left:285px;top:153px"></div>
    <div class="stamp" style="left:492px;top:153px"></div>
    <div class="stamp" style="left:78px;top:301px"></div>
    <div class="stamp" style="left:285px;top:301px"></div>
    <div class="stamp" style="left:492px;top:301px"></div>
    <div class="brand-name back-brand">QuayBite</div>
    <div class="stamp stamp-free" style="left:701px;top:301px">FREE</div>
    <p class="footer-note not-transferable">Not Transferable</p>
    <p class="footer-note valid-till">Over Valid till:</p>
    <div class="valid-field"></div>
  </section>
</div>
</body>
</html>
```